Keystone Allies Website

My business has been word of mouth over the last 3 years and has grown. Now I need a website for additional marketing as we have new clients asking for a website.

You have already completed my Logo during an earlier project. I have attached the logo.

We do Staff Augmentation and Operation Support.

What is that?
Staff augmentation is an outsourcing strategy that allows companies to fill specific, temporary roles to achieve business objectives. This staffing method complements existing teams with specific talent, enhancing business capabilities or filling gaps left by members on extended leave.

We work alongside the internal recruiting team to assist clients to meet and exceed financial goals.

```html
<!DOCTYPE html>
<html lang="en">
<head>
<meta charset="utf-8">
<title>Keystone Allies</title>
<link href="https://fonts.googleapis.com/css2?family=Poppins:wght@300;400;500;600&display=swap" rel="stylesheet">
<style>
:root{
  --navy:#0f4d78;
  --navy-dark:#0c456d;
  --grey-title:#6d6d6d;
  --text:#8a8a8a;
  --panel:#f6f6f6;
  --line:#d9d9d9;
  --white:#fff;
}
*{box-sizing:border-box;margin:0;padding:0}
html,body{width:1200px;height:3509px;overflow:hidden;background:var(--white);font-family:'Poppins',sans-serif;color:var(--text)}
.page{position:relative;width:1200px;height:3509px}
.abs{position:absolute}

/* header */
.site-header{position:absolute;top:0;left:0;width:1200px;height:82px}
.brand{position:absolute;left:60px;top:16px;display:flex;align-items:center;gap:10px;color:var(--navy);font-weight:600;font-size:24px;letter-spacing:.5px}
.brand-dot{width:44px;height:44px;border-radius:50%;background:var(--navy)}
.main-nav{position:absolute;left:413px;top:30px;display:flex;gap:32px;font-size:13px;font-weight:500;color:#777}
.main-nav .active{color:var(--navy)}
.header-phone{position:absolute;left:952px;top:17px;width:188px;height:44px;border-radius:22px;background:var(--navy);color:#fff;font-size:13px;font-weight:500;display:flex;align-items:center;justify-content:center;gap:8px}

/* hero */
.hero-photo{position:absolute;top:82px;left:0;width:1200px;height:615px;background:linear-gradient(90deg,#d8d2cc 0%,#e4dfda 48%,#f4f4f4 50.5%,#fbfbfb 100%)}
.hero-title{position:absolute;left:61px;top:200px;font-size:47px;line-height:54px;font-weight:600;color:var(--navy)}
.hero-text{position:absolute;left:61px;top:384px;font-size:13.5px;line-height:27px;color:#333}
.btn{display:flex;align-items:center;justify-content:center;background:var(--navy);color:#fff;font-weight:500;border-radius:24px;letter-spacing:.3px}
.hero-btn{position:absolute;left:60px;top:483px;width:150px;height:44px;font-size:12px}

.contact-bar{position:absolute;left:214px;top:660px;width:772px;height:75px;border-radius:38px;background:#808080;overflow:hidden}
.contact-bar .call{position:absolute;left:0;top:0;width:406px;height:75px;background:var(--navy);display:flex;align-items:center;padding-left:36px;gap:12px;color:#fff}
.call small{font-size:15px}
.call strong{font-size:26px;font-weight:500}
.contact-bar .mid{position:absolute;left:367px;top:0;width:76px;height:75px;border-radius:50%;background:#fff}
.contact-bar .mail{position:absolute;left:468px;top:0;height:75px;display:flex;align-items:center;gap:12px;color:#fff;font-size:17px}

/* welcome */
.section-title{position:absolute;left:0;width:1200px;text-align:center;font-size:44px;font-weight:600;color:var(--grey-title);letter-spacing:.5px}
.section-title span{color:var(--navy)}
.welcome-text{position:absolute;left:170px;top:883px;width:860px;text-align:center;font-size:13.5px;line-height:26.5px}
.see-how{position:absolute;left:0;top:1010px;width:1200px;text-align:center;font-size:17px;font-weight:500;color:var(--navy)}
.get-touch{position:absolute;left:0;top:1053px;width:1200px;display:flex;justify-content:center;align-items:center;gap:12px;font-size:25px;font-weight:500;color:var(--grey-title)}
.get-touch b{color:var(--navy);font-weight:500}
.or{position:absolute;left:0;top:1102px;width:1200px;text-align:center;font-size:12px}
.field{position:absolute;border:1px solid var(--line);border-radius:4px;font-size:14px;color:#999;padding:12px 12px}
.send{position:absolute;left:518px;top:1382px;width:164px;height:44px;font-size:12px}

/* services */
.service-photo{position:absolute;width:540px;height:397px}
.service-panel{position:absolute;width:540px;height:397px;background:var(--panel)}
.service-panel h3{position:absolute;font-size:38px;font-weight:500;color:var(--navy)}
.service-panel p{position:absolute;font-size:13.5px;line-height:26.3px}

/* advantages */
.adv-card{position:absolute;top:2577px;width:338px;height:555px;background:var(--panel)}
.adv-card .photo{width:338px;height:240px}
.adv-card h4{margin:17px 15px 0;font-size:17px;font-weight:500;color:#444}
.adv-card p{margin:6px 15px 0;font-size:11.5px;line-height:22.5px}

/* footer */
.site-footer{position:absolute;left:0;top:3252px;width:1200px;height:257px;background:var(--navy-dark);color:#fff}
.foot-brand{position:absolute;left:60px;top:38px;display:flex;align-items:center;gap:12px;font-size:32px;font-weight:500;line-height:30px}
.foot-brand .brand-dot{width:60px;height:60px;background:#fff}
.foot-addr{position:absolute;left:60px;top:122px;width:240px;text-align:center;font-size:12px;line-height:22px}
.foot-links{position:absolute;left:338px;top:38px;list-style:none;font-size:12px;line-height:30px}
.foot-info{position:absolute;left:614px;top:38px;font-size:12px;line-height:22px}
.foot-info div{display:flex;gap:8px}
.foot-touch{position:absolute;left:893px;top:38px;font-size:12px}
.foot-touch h5{font-size:13px;font-weight:500;margin-bottom:14px}
.copyright{position:absolute;left:0;top:3480px;width:1200px;text-align:center;font-size:11px;color:#c9d6e0}
</style>
</head>
<body>
<div class="page">

<header class="site-header">
  <div class="brand"><span class="brand-dot"></span>KEYSTONE ALLIES</div>
  <nav class="main-nav"><span class="active">HOME</span><span>ABOUT</span><span>SERVICES</span><span>NEWS</span><span>CONTACT</span></nav>
  <div class="header-phone">
    <svg width="16" height="16" viewBox="0 0 24 24"><path fill="#fff" d="M6.6 10.8a15 15 0 006.6 6.6l2.2-2.2c.3-.3.7-.4 1-.2 1.1.4 2.3.6 3.6.6.6 0 1 .4 1 1V20c0 .6-.4 1-1 1C10.6 21 3 13.4 3 4c0-.6.4-1 1-1h3.5c.6 0 1 .4 1 1 0 1.3.2 2.5.6 3.6.1.3 0 .7-.2 1z"/></svg>
    (800) 555-0148
  </div>
</header>

<section class="hero">
  <div class="hero-photo" role="img" aria-label="Overhead photo of two professionals shaking hands across a white desk with a laptop and papers"></div>
  <h1 class="hero-title">Find a perfect<br>candidate for<br>your projects</h1>
  <p class="hero-text">We do Staff Augmentation and Operation Support.<br>We will work alongside your recruiting and operation<br>teams to assist you to meet and exceed financial goals.</p>
  <div class="btn hero-btn">CONTACT US</div>
  <div class="contact-bar">
    <div class="call">
      <small>CALL US</small>
      <svg width="26" height="26" viewBox="0 0 24 24"><path fill="#fff" d="M6.6 10.8a15 15 0 006.6 6.6l2.2-2.2c.3-.3.7-.4 1-.2 1.1.4 2.3.6 3.6.6.6 0 1 .4 1 1V20c0 .6-.4 1-1 1C10.6 21 3 13.4 3 4c0-.6.4-1 1-1h3.5c.6 0 1 .4 1 1 0 1.3.2 2.5.6 3.6.1.3 0 .7-.2 1z"/></svg>
      <strong>(800) 555-0148</strong>
    </div>
    <div class="mid"></div>
    <div class="mail">
      <svg width="26" height="20" viewBox="0 0 26 20"><rect x="1" y="1" width="24" height="18" rx="2" fill="none" stroke="#fff" stroke-width="2"/><path d="M1 2l12 9 12-9" fill="none" stroke="#fff" stroke-width="2"/></svg>
      info@keystoneallies.biz
    </div>
  </div>
</section>

<section class="welcome">
  <h2 class="section-title" style="top:815px">WELCOME TO <span>KEYSTONE ALLIES</span></h2>
  <p class="welcome-text">With over 45 years of experience in outsourcing within the BPO environment, Keystone Allies delivers Operational and Sales customer solutions for global organizations. We do this by building sustainable cultural and talent management programs and managing key stakeholders and clients, locally and internationally. We drive operational excellence and achieve both growth and customer delivery targets, making Keystone Allies an outstanding resource for your company's growth.</p>
  <p class="see-how">See how Keystone Allies can help you business.</p>
  <div class="get-touch">GET IN TOUCH
    <svg width="26" height="26" viewBox="0 0 24 24"><path fill="#0f4d78" d="M6.6 10.8a15 15 0 006.6 6.6l2.2-2.2c.3-.3.7-.4 1-.2 1.1.4 2.3.6 3.6.6.6 0 1 .4 1 1V20c0 .6-.4 1-1 1C10.6 21 3 13.4 3 4c0-.6.4-1 1-1h3.5c.6 0 1 .4 1 1 0 1.3.2 2.5.6 3.6.1.3 0 .7-.2 1z"/></svg>
    <b>(800) 555-0148</b></div>
  <div class="or">OR</div>
  <div class="field" style="left:278px;top:1142px;width:314px;height:45px">Name</div>
  <div class="field" style="left:608px;top:1142px;width:314px;height:45px">Contact No.</div>
  <div class="field" style="left:278px;top:1202px;width:644px;height:45px">Email*</div>
  <div class="field" style="left:278px;top:1262px;width:644px;height:105px">Message</div>
  <div class="btn send">SEND MESSAGE</div>
</section>

<section class="services">
  <h2 class="section-title" style="top:1512px">OUR <span>SERVICES</span></h2>
  <div class="service-photo" style="left:60px;top:1605px;background:linear-gradient(135deg,#8a8f88,#c9cfd2 60%,#e4e8ea)" role="img" aria-label="Photo of a smiling man working on a laptop in a bright office"></div>
  <div class="service-panel" style="left:600px;top:1605px">
    <h3 style="left:40px;top:38px">Staff Augmentation</h3>
    <p style="left:40px;top:90px;width:470px">We see staff augmentation as an extension of your internal team's recruiting arm. It is simply about temporarily hiring an expert resource to supplement the in-house team. The model will fill the gaps you have in your staffing. The process is relatively simple: you call us, discuss your project, and we find the personnel for your project. Those employees then come and work from home or at your office. Their tenure is as long as agreed upon. The staff hired is an expert resource which means that the company doesn't have to waste time and money training the staff, rather he/she will have the experience and expertise required to complete the project right away.</p>
  </div>
  <div class="service-panel" style="left:60px;top:2002px">
    <h3 style="left:39px;top:52px">Operation Support</h3>
    <p style="left:39px;top:114px;width:460px">A cost-effective solution for deploying portions of your business with another supplier who specializes in a service that helps exceed your financial or customer experience goals.</p>
    <p style="left:39px;top:220px;width:450px">Our experience in contact center services allows us to recognize how to simplify, secure, and make the process profitable. We use technological and multi-channel tools to efficiently reach your clients, maintain security and uphold strict privacy standards in accordance with the regulations of each territory.</p>
  </div>
  <div class="service-photo" style="left:600px;top:2002px;background:linear-gradient(135deg,#6e7275,#b9bcbd 55%,#e6e6e4)" role="img" aria-label="Photo of a smiling call center agent wearing a headset"></div>
</section>

<section class="advantages">
  <h2 class="section-title" style="top:2494px;color:var(--navy)">ADAVANTAGES</h2>
  <article class="adv-card" style="left:60px">
    <div class="photo" style="background:linear-gradient(135deg,#1f3a4d,#3c6f8c 50%,#0e1a22)" role="img" aria-label="Close-up of a compass pointing toward the word talent"></div>
    <h4 style="margin-top:24px">Reducing Recruiting Timelines</h4>
    <p>You get qualified professionals, working in your office or at home, at your desired times, and on your desired projects in a matter of weeks. If you've got an existing team, it's easy for staff augmentation to provide temporary employees who can transition into full-time employees of your organization if needed. Allows organizations to skip the qualification process. You only get qualified professionals who have been fully screened and passed the initial requirements</p>
  </article>
  <article class="adv-card" style="left:431px">
    <div class="photo" style="background:linear-gradient(135deg,#b8bcc0,#e3e5e7 55%,#9da2a6)" role="img" aria-label="Photo of a businesswoman standing in a modern office"></div>
    <h4>Flexibility</h4>
    <p>In today's competitive and rather hostile business environment, businesses need the flexibility to stay relevant and grow. Staff augmentation helps businesses to expand their portfolios to non-core services as well, by simply taking on-board an expert staff to complement the in-house team. This gives businesses the flexibility and agility required to remain relevant in the industry.</p>
  </article>
  <article class="adv-card" style="left:802px">
    <div class="photo" style="background:linear-gradient(135deg,#3a3a3a,#9a9793 50%,#d9d6d1)" role="img" aria-label="Photo of a job candidate in an interview holding a résumé"></div>
    <h4>Counteracting attrition</h4>
    <p>Staff augmentation acts as a great deterrence against employees leaving the company. One study suggests that nearly 50% of all specialists are open to switching companies when provided with better opportunities or greater perks. This may leave businesses with great voids in human resources and staff augmentation is perhaps the best way to quickly fill up the leftover position without wasting precious time and resources.</p>
  </article>
</section>

<footer class="site-footer">
  <div class="foot-brand"><span class="brand-dot"></span><span>KEYSTONE<br>ALLIES</span></div>
  <p class="foot-addr">Ashford, IA office address where the LLC. is registered</p>
  <ul class="foot-links"><li>Home</li><li>About</li><li>Services</li><li>News</li><li>Contact Us</li></ul>
  <div class="foot-info">
    <div><svg width="12" height="16" viewBox="0 0 12 16"><path fill="#fff" d="M6 0a6 6 0 00-6 6c0 4.5 6 10 6 10s6-5.5 6-10a6 6 0 00-6-6zm0 8.5A2.5 2.5 0 116 3.5a2.5 2.5 0 010 5z"/></svg><span>Lorem Ipsum is simply dummy text<br>of the printing</span></div>
    <div style="margin-top:10px"><svg width="14" height="14" viewBox="0 0 24 24"><path fill="#fff" d="M6.6 10.8a15 15 0 006.6 6.6l2.2-2.2c.3-.3.7-.4 1-.2 1.1.4 2.3.6 3.6.6.6 0 1 .4 1 1V20c0 .6-.4 1-1 1C10.6 21 3 13.4 3 4c0-.6.4-1 1-1h3.5c.6 0 1 .4 1 1 0 1.3.2 2.5.6 3.6.1.3 0 .7-.2 1z"/></svg><b style="font-weight:500">(800) 555-0148</b></div>
  </div>
  <div class="foot-touch">
    <h5>GET IN TOUCH</h5>
    <div style="display:flex;gap:8px;align-items:center"><svg width="16" height="12" viewBox="0 0 26 20"><rect x="1" y="1" width="24" height="18" rx="2" fill="#fff"/><path d="M1 2l12 9 12-9" fill="none" stroke="#0c456d" stroke-width="2"/></svg>info@keystoneallies.biz</div>
  </div>
</footer>
<p class="copyright">© KEYSTONE ALLIES - 2022. All Rights Reserved.</p>

</div>
</body>
</html>
```